Flyer for Pharmacy/Medical Convention

Tri-fold flyer for pharmacy/medical convention. The inside of the flyer we would like to look like a venn diagram, possibly using an image similar to our blue logo

Copy write will be submitted when a design is chosen

there will be a flap about educational features, one about supplements an automated recommendations, and a flap about a computer platform to manage patients

Target Market(s)

Pharmacists and Medical Providers

Industry/Entity Type

Supplement

Colors

Designer to choose colors to be used in the design.

Requirements
Must have
• color scheme similar to logos and or label design attached

```html
<!DOCTYPE html>
<html lang="en">
<head>
<meta charset="utf-8">
<title>Clearwell Solutions – Tri-fold Flyer</title>
<link rel="stylesheet" href="https://fonts.googleapis.com/css2?family=Open+Sans:wght@300;400;600;700;800&family=Roboto:wght@300;400;500&family=Roboto+Condensed:wght@700&display=swap">
<style>
  :root {
    --navy: #27307f;
    --navy-deep: #141a4d;
    --blue: #2264b4;
    --blue-text: #2b5ea8;
    --paper: #f4f5f8;
    --grey-text: #555a66;
    --white: #ffffff;
  }
  * { box-sizing: border-box; margin: 0; padding: 0; }
  html, body { width: 1200px; height: 864px; overflow: hidden; background: #d8d9dc; }
  .flyer { position: relative; width: 1200px; height: 864px; overflow: hidden; background: var(--paper); font-family: "Open Sans", sans-serif; }
  .panel { position: absolute; top: 0; width: 400px; height: 864px; overflow: hidden; }
  .panel--left { left: 0; background: var(--white); }
  .panel--middle { left: 400px; background: var(--paper); }
  .panel--right { left: 800px; background: var(--white); }
  .panel-shape { position: absolute; inset: 0; }

  /* left panel */
  .section-title { position: absolute; left: 35px; top: 42px; color: var(--blue-text); line-height: 1; }
  .section-title strong { display: block; font-size: 27px; font-weight: 700; letter-spacing: .5px; }
  .section-title span { display: block; font-size: 25px; font-weight: 300; color: #3e4a72; margin-top: 1px; }
  .section-title::after { content: ""; display: block; width: 110px; height: 2px; background: var(--blue-text); margin-top: 3px; }
  .feature { position: absolute; left: 35px; width: 340px; }
  .feature-icon { position: absolute; left: 0; top: 0; width: 44px; height: 40px; }
  .feature-title { margin-left: 52px; font-size: 19px; font-weight: 700; color: var(--blue-text); display: inline-block; border-bottom: 2px solid var(--blue-text); line-height: 1.2; }
  .feature-text { margin-left: 52px; margin-top: 8px; font-size: 13px; line-height: 1.2; color: var(--grey-text); }
  .photo-ring { position: absolute; border-radius: 50%; border: 7px solid var(--navy); overflow: hidden; }
  .photo-ring--main { left: 108px; top: 309px; width: 246px; height: 246px; background: radial-gradient(circle at 45% 40%, #f6f6f6, #cfd0d4 55%, #8f9196); }
  .photo-ring--product { left: 43px; top: 444px; width: 104px; height: 104px; border-width: 5px; background: radial-gradient(circle at 50% 45%, #ffffff, #d7dae6 60%, #8e95b8); }
  .footer-band { position: absolute; left: 0; bottom: 0; width: 400px; height: 64px; background: linear-gradient(90deg, var(--navy-deep), #1c2566); }
  .footer-url { position: absolute; left: 44px; top: 20px; font-size: 17px; font-weight: 700; color: #3a6cc0; }

  /* middle panel */
  .hero-title { position: absolute; left: 40px; top: 34px; color: var(--white); font-family: "Roboto", sans-serif; }
  .hero-title h2 { font-size: 37px; font-weight: 400; letter-spacing: .5px; line-height: 1; }
  .hero-title p { font-size: 18px; font-weight: 400; margin-top: 8px; letter-spacing: .3px; }
  .bullets { position: absolute; list-style: none; color: var(--white); }
  .bullets li { position: relative; padding-left: 20px; line-height: 1.25; }
  .bullets li::before { content: ""; position: absolute; left: 2px; top: 6px; width: 6px; height: 6px; background: var(--white); }
  .bullets--middle { left: 40px; top: 128px; width: 330px; font-size: 13px; }
  .bullets--middle li + li { margin-top: 16px; }
  .badge { position: absolute; left: 31px; top: 306px; width: 220px; height: 220px; border-radius: 50%; background: var(--white); border: 8px solid var(--navy); box-shadow: 0 0 0 3px rgba(255,255,255,.6); text-align: center; padding-top: 42px; }
  .badge strong { display: inline-block; font-family: "Roboto Condensed", sans-serif; font-size: 37px; color: var(--navy); border-bottom: 2px solid var(--navy); line-height: 1.05; padding: 0 10px 2px; }
  .badge span { display: block; font-family: "Roboto", sans-serif; font-size: 25px; color: var(--blue); line-height: 1.2; margin-top: 4px; }
  .rail-scene { position: absolute; left: 0; top: 470px; width: 400px; height: 394px; background: linear-gradient(180deg, rgba(244,245,248,0) 0%, #dfe3f0 40%, #b3bde0 75%, #6d7fc4 100%); }
  .sub-title { position: absolute; left: 40px; top: 545px; color: var(--navy); }
  .sub-title strong { display: block; font-size: 23px; font-weight: 700; line-height: 1.05; }
  .sub-title span { display: inline-block; font-size: 16px; font-weight: 600; color: #3a3f5a; letter-spacing: .3px; line-height: 1.2; }
  .sub-title span::after { content: ""; display: block; width: 70px; height: 2px; background: var(--navy); margin-top: 2px; }
  .service-item { position: absolute; left: 36px; width: 340px; }
  .service-icon { position: absolute; left: 0; top: 0; width: 52px; height: 52px; border-radius: 50%; background: linear-gradient(135deg, #3a78c8, var(--navy)); }
  .service-icon svg { position: absolute; left: 12px; top: 12px; }
  .service-title { margin-left: 66px; font-size: 18px; font-weight: 700; color: var(--blue-text); display: inline-block; border-bottom: 2px solid var(--blue-text); line-height: 1.2; }
  .service-text { margin-left: 66px; margin-top: 7px; font-size: 12.5px; line-height: 1.25; color: #3e4358; }

  /* right panel */
  .runners-photo { position: absolute; left: 0; top: 380px; width: 400px; height: 484px; background: linear-gradient(160deg, #c8cdb4 0%, #9aa58a 35%, #b36a86 60%, #6d5a5e 85%, #3c3c44 100%); }
  .food-photo { position: absolute; left: 282px; top: -32px; width: 128px; height: 128px; border-radius: 50%; border: 5px solid var(--white); background: radial-gradient(circle at 40% 55%, #7aa45a, #c8482c 45%, #b7814c 80%); }
  .service-heading { position: absolute; left: 40px; top: 40px; color: var(--white); line-height: 1; }
  .service-heading strong { display: block; font-size: 27px; font-weight: 700; }
  .service-heading span { display: block; font-size: 27px; font-weight: 300; }
  .service-heading::after { content: ""; display: block; width: 58px; height: 2px; background: var(--white); margin-top: 4px; }
  .bullets--right { left: 40px; top: 114px; width: 320px; font-size: 13.5px; }
  .bullets--right li { line-height: 1.22; }
  .bullets--right li + li { margin-top: 8px; }
  .tagline { position: absolute; left: 40px; top: 288px; color: var(--white); font-size: 15.5px; line-height: 1.3; }
  .tagline .light { font-weight: 300; }
  .tagline .bold { font-weight: 800; letter-spacing: .3px; }
  .tagline .gap { margin-top: 8px; }
</style>
</head>
<body>
<main class="flyer">

  <!-- Panel: educational features -->
  <section class="panel panel--left">
    <svg class="panel-shape" width="400" height="864" viewBox="0 0 400 864" aria-hidden="true">
      <defs>
        <linearGradient id="leftWash" x1="0" y1="0" x2="1" y2="0">
          <stop offset="0" stop-color="#c6cadd"/>
          <stop offset="1" stop-color="#eceef4"/>
        </linearGradient>
      </defs>
      <rect width="400" height="864" fill="#f2f3f6"/>
      <path d="M0 0 H372 C 300 190, 300 520, 400 760 V800 H0 Z" fill="url(#leftWash)"/>
      <path d="M0 480 C 120 620, 260 720, 400 790 V800 H0 Z" fill="#ffffff" opacity=".55"/>
    </svg>

    <h2 class="section-title"><strong>EDUCATIONAL</strong><span>FEATURES</span></h2>

    <div class="feature" style="top:118px">
      <svg class="feature-icon" viewBox="0 0 44 40" fill="none" stroke="#27307f" stroke-width="2.2" aria-hidden="true">
        <rect x="4" y="12" width="30" height="20" rx="2"/><line x1="4" y1="18" x2="34" y2="18"/>
        <path d="M10 8 L38 4 L40 22 L34 23"/><line x1="9" y1="27" x2="17" y2="27"/>
      </svg>
      <h3 class="feature-title">Lorem Ipsum</h3>
      <p class="feature-text">Lorem ipsum dolor sit amet, consectetur adip-iscing elit, sed do eiusmod tempor incididunt ut.</p>
    </div>

    <div class="feature" style="top:214px">
      <svg class="feature-icon" viewBox="0 0 44 40" fill="none" stroke="#27307f" stroke-width="2" aria-hidden="true">
        <circle cx="20" cy="15" r="11"/><path d="M21 8 L16 16 H23 L18 23"/>
        <line x1="15" y1="30" x2="25" y2="30"/><line x1="16" y1="34" x2="24" y2="34"/>
      </svg>
      <h3 class="feature-title">Lorem Ipsum</h3>
      <p class="feature-text">Lorem ipsum dolor sit amet, consectetur adip-iscing elit, sed do eiusmod tempor incididunt ut.</p>
    </div>

    <div class="photo-ring photo-ring--main" role="img" aria-label="Photo of a tired worker resting his head under a laptop on a desk"></div>
    <div class="photo-ring photo-ring--product" role="img" aria-label="Photo of a supplement bottle"></div>

    <div class="feature" style="top:600px">
      <svg class="feature-icon" viewBox="0 0 44 40" fill="none" stroke="#27307f" stroke-width="2" aria-hidden="true">
        <polyline points="4,4 4,34 38,34"/><polyline points="8,28 16,20 22,24 34,12"/>
      </svg>
      <h3 class="feature-title">Lorem Ipsum</h3>
      <p class="feature-text">Lorem ipsum dolor sit amet, consectetur adip-iscing elit, sed do eiusmod tempor incididunt ut.</p>
    </div>

    <div class="feature" style="top:694px">
      <svg class="feature-icon" viewBox="0 0 44 40" fill="none" stroke="#27307f" stroke-width="2" aria-hidden="true">
        <circle cx="17" cy="8" r="3"/><line x1="15" y1="11" x2="8" y2="34"/><line x1="19" y1="11" x2="26" y2="34"/>
        <path d="M8 24 Q17 30 26 24"/>
      </svg>
      <h3 class="feature-title">Lorem Ipsum</h3>
      <p class="feature-text">Lorem ipsum dolor sit amet, consectetur adip-iscing elit, sed do eiusmod tempor incididunt ut.</p>
    </div>

    <footer class="footer-band"><span class="footer-url">www.ClearwellSolutions.com</span></footer>
  </section>

  <!-- Panel: supplements and automated recommendations -->
  <section class="panel panel--middle">
    <div class="rail-scene" role="img" aria-label="Soft blue photo of railway tracks fading into the distance"></div>
    <svg class="panel-shape" width="400" height="864" viewBox="0 0 400 864" aria-hidden="true">
      <path d="M0 0 H400 V490 H210 C 120 490, 40 420, 0 340 Z" fill="#2264b4"/>
    </svg>

    <header class="hero-title">
      <h2>LOREM IPSUM</h2>
      <p>PLACE YOUR TEXT HERE</p>
    </header>
    <ul class="bullets bullets--middle">
      <li>Recognizing a need for a line of nutritional supple-ments designed by health care professionals, for health care professionals, Summit Clearwell Solutions was created.</li>
      <li>Recognizing a need for a line of nutritional supple-ments designed by health care professionals, for health care professionals, Summit Clearwell Solutions was created.</li>
    </ul>

    <div class="badge">
      <strong>RESEARCH</strong>
      <span>Based formulas<br>at therapeutic<br>Dosages</span>
    </div>

    <h2 class="sub-title"><strong>SUPPLEMENTS AN</strong><span>AUTOMATED RECOMMENDATIONS</span></h2>

    <div class="service-item" style="top:614px">
      <div class="service-icon"><svg width="28" height="28" viewBox="0 0 28 28" fill="none" stroke="#fff" stroke-width="1.6" aria-hidden="true"><circle cx="14" cy="8" r="3"/><circle cx="6" cy="11" r="2.5"/><circle cx="22" cy="11" r="2.5"/><path d="M9 22 V16 Q14 12 19 16 V22"/><path d="M2 22 V18 Q6 15 9 17"/><path d="M26 22 V18 Q22 15 19 17"/></svg></div>
      <h3 class="service-title">Lorem Ipsum</h3>
      <p class="service-text">Lorem ipsum dolor sit amet, consectetuer adipiscing elit, sed diam nonummy.</p>
    </div>
    <div class="service-item" style="top:696px">
      <div class="service-icon"><svg width="28" height="28" viewBox="0 0 28 28" fill="none" stroke="#fff" stroke-width="1.8" aria-hidden="true"><circle cx="16" cy="11" r="8"/><line x1="10" y1="17" x2="3" y2="24"/></svg></div>
      <h3 class="service-title">Lorem Ipsum</h3>
      <p class="service-text">Lorem ipsum dolor sit amet, consectetuer adipiscing elit, sed diam nonummy.</p>
    </div>
    <div class="service-item" style="top:776px">
      <div class="service-icon"><svg width="28" height="28" viewBox="0 0 28 28" fill="none" stroke="#fff" stroke-width="1.6" aria-hidden="true"><path d="M24 4 Q14 5 9 15 L13 19 Q23 14 24 4 Z"/><circle cx="17" cy="11" r="2"/><path d="M9 15 L4 15 L8 11"/><path d="M13 19 L13 24 L17 20"/><path d="M7 21 L4 24"/></svg></div>
      <h3 class="service-title">Lorem Ipsum</h3>
      <p class="service-text">Lorem ipsum dolor sit amet, consectetuer adipiscing elit, sed diam nonummy.</p>
    </div>
  </section>

  <!-- Panel: our service -->
  <section class="panel panel--right">
    <div class="runners-photo" role="img" aria-label="Photo of a smiling woman and man jogging outdoors"></div>
    <svg class="panel-shape" width="400" height="864" viewBox="0 0 400 864" aria-hidden="true">
      <defs>
        <linearGradient id="serviceBlue" x1="0" y1="0" x2="1" y2="0">
          <stop offset="0" stop-color="#2b3592"/>
          <stop offset="1" stop-color="#2366b6"/>
        </linearGradient>
      </defs>
      <path d="M0 0 H400 V110 C 370 320, 200 460, 0 490 Z" fill="url(#serviceBlue)"/>
      <path d="M400 770 V864 H300 Z" fill="#2a2a30"/>
    </svg>
    <div class="food-photo" role="img" aria-label="Photo of fresh vegetables on a wooden board"></div>

    <h2 class="service-heading"><strong>OUR</strong><span>SERVICE</span></h2>
    <ul class="bullets bullets--right">
      <li>Ostrelle QX is an advanced, professional grade, plant-sourced calcium and bone building formula exclusively available through healthcare professionals.</li>
      <li>The highly specialized plant calcium in Ostrelle QX is micronized to ensure optimal absorption by delivering the perfect particle size.</li>
    </ul>
    <div class="tagline">
      <p class="light">While your physicians are adding</p>
      <p class="bold">YEARS TO YOUR LIFE,</p>
      <p class="light gap">we at Clearwell Solutions</p>
      <p class="bold">ARE ADDING<br>LIFE TO YOUR YEARS</p>
    </div>
  </section>

</main>
</body>
</html>
```